ZY3 ‘Unlock Your QM8 success code’

‘Unlock Your QM8 success code ‘ this pay of ok , and also the logo, but i need a cover for one pdf A4, ZY3 is a product for discovery the skill in human resource

See below link to serve as inspiration reference in creating your design proposals. Thank you.

zy3careerlab.com
Updates

ce systeme sketchhive pas tros claire,j ai acheter 70 dessins et ont me demande contuement des trucs a faire bah

Target Market(s)

https://qm8careerlab.com/available-reports/ i work for this company

Industry/Entity Type

Business Consultant

Font styles to use
Serif

Colors
3176b5
3276b5
6cbee2
85abd2
3277b5

Requirements
Must have
• Look the link and product Report ZY3, i need professional and istutional look And on cover ‘Unlock your QM8 success code’
Nice to have
• front blue and Grey , silver, look my files , i need the silver Logo Qm8 , Genotric stile
Should not have
• fantasy,

```html
<!DOCTYPE html>
<html lang="en">
<head>
<meta charset="utf-8">
<title>Unlock Your ZY3 Success Code – Report Cover</title>
<link href="https://fonts.googleapis.com/css2?family=Oswald:wght@400;600&display=swap" rel="stylesheet">
<style>
  :root {
    --backdrop: #e9eef2;
    --cover-black: #000000;
    --title-white: #e8e8e8;
    --brand-blue: #58a7d3;
    --ring-white: #f2f2f2;
    --logo-silver: #d4d6d8;
    --earth-dark: #3a2a1c;
    --earth-mid: #6b4c30;
    --sky-blue: #4f7fa6;
    --sky-haze: #c9c3a6;
    --sun-gold: #e6b42c;
    --sand-dark: #4a3a1c;
  }
  * { margin: 0; padding: 0; box-sizing: border-box; }
  html, body {
    width: 1180px;
    height: 1200px;
    overflow: hidden;
    background: var(--backdrop);
  }
  .cover {
    position: absolute;
    left: 196px;
    top: 39px;
    width: 788px;
    height: 1122px;
    background: var(--cover-black);
    overflow: hidden;
    font-family: "Oswald", "Arial Narrow", sans-serif;
  }
  .title-main {
    position: absolute;
    left: 62px;
    top: 23px;
    font-weight: 600;
    font-size: 248px;
    line-height: 1;
    letter-spacing: -5px;
    white-space: nowrap;
    color: var(--title-white);
    transform: scaleX(0.86);
    transform-origin: left top;
  }
  .title-main .accent { color: var(--brand-blue); }
  .title-rule {
    position: absolute;
    left: 65px;
    top: 290px;
    width: 663px;
    height: 3px;
    background: var(--title-white);
  }
  .subtitle {
    position: absolute;
    left: 63px;
    white-space: nowrap;
    font-weight: 400;
    line-height: 1;
    transform-origin: left top;
  }
  .subtitle-product {
    top: 306px;
    font-size: 133px;
    color: var(--title-white);
    transform: scaleX(0.86);
  }
  .subtitle-code {
    top: 445px;
    font-size: 134px;
    color: var(--brand-blue);
    transform: scaleX(0.89);
  }
  .cover-art {
    position: absolute;
    left: 0;
    top: 0;
    width: 788px;
    height: 1122px;
  }
  .brand-mark {
    position: absolute;
    left: 236px;
    top: 886px;
    transform: translate(-50%, -50%);
    display: flex;
    align-items: center;
    gap: 12px;
    font-weight: 600;
    font-size: 52px;
    line-height: 1;
    color: var(--logo-silver);
  }
  .brand-mark .brand-dot {
    width: 22px;
    height: 22px;
    border-radius: 50%;
    background: var(--logo-silver);
  }
</style>
</head>
<body>
  <main class="cover">
    <h1 class="title-main">UN<span class="accent">LOCK</span></h1>
    <div class="title-rule"></div>
    <p class="subtitle subtitle-product">YOUR ZY3</p>
    <p class="subtitle subtitle-code">SUCCESS CODE</p>

    <svg class="cover-art" viewBox="0 0 788 1122" xmlns="http://www.w3.org/2000/svg">
      <defs>
        <linearGradient id="sunset-fill" x1="0" y1="0" x2="0" y2="1">
          <stop offset="0" stop-color="var(--sky-blue)"/>
          <stop offset="0.3" stop-color="var(--sky-haze)"/>
          <stop offset="0.55" stop-color="var(--sun-gold)"/>
          <stop offset="1" stop-color="var(--sand-dark)"/>
        </linearGradient>
        <radialGradient id="earth-fill" cx="0.5" cy="0.5" r="0.6">
          <stop offset="0" stop-color="var(--earth-mid)"/>
          <stop offset="1" stop-color="var(--earth-dark)"/>
        </radialGradient>
      </defs>
      <g class="sunset-photo" role="img" aria-label="Photo: people jumping joyfully on a beach at sunset">
        <circle cx="573" cy="948" r="328" fill="url(#sunset-fill)" stroke="var(--ring-white)" stroke-width="6"/>
      </g>
      <g class="key-photo" role="img" aria-label="Photo: a key lying among dry leaves on the forest floor">
        <circle cx="236" cy="886" r="185" fill="url(#earth-fill)" stroke="var(--brand-blue)" stroke-width="6"/>
      </g>
    </svg>

    <div class="brand-mark"><span class="brand-dot"></span>ZY3</div>
  </main>
</body>
</html>
```